KMR Info Brochure

We need a brochure design for a new not-for-profit organisation that is aimed at providing homeless people with a residence that also provides counselling and vocational training to assist them to find suitable employment at the end of the program.
PLEASE NOTE:
Brochure to be A4.
I know the brochure is quite long, it is really a booklet, but please note that it does not have to have a lot of work done on it, I just want it to look professional and the front cover and inside page to look good.
Also please leave about 2-3 pages at the end as I will be adding in some architect drawings.
Please add in a last page with Contact written at the bottom - we will fill that in later. So please ensure it is editable in PDF.
Thank you so much.
Cheers
Petra

```html
<!DOCTYPE html>
<html lang="en">
<head>
<meta charset="utf-8">
<title>KMR Info Brochure – Executive Summary Spread</title>
<link href="https://fonts.googleapis.com/css2?family=Marcellus&family=Hind:wght@400;500&display=swap" rel="stylesheet">
<style>
  :root {
    --backdrop: #2b2b2d;
    --navy: #0f2a66;
    --navy-deep: #0b2058;
    --spine-light: #e8ecf4;
    --gold: #e7b73b;
    --gold-deep: #d9a21f;
    --paper: #ffffff;
    --text-light: #f4f6fb;
    --photo-top: #6d7078;
    --photo-mid: #3d3f46;
    --photo-warm: #d9826f;
    --photo-olive: #5f6448;
  }
  * { box-sizing: border-box; margin: 0; padding: 0; }
  html, body { width: 1200px; height: 860px; overflow: hidden; }
  body {
    background: var(--backdrop);
    font-family: "Hind", Arial, sans-serif;
    display: flex;
    align-items: center;
    justify-content: center;
  }
  .spread {
    width: 1100px;
    height: 780px;
    display: flex;
    box-shadow: 0 10px 30px rgba(0,0,0,.45);
  }
  .page {
    position: relative;
    width: 550px;
    height: 780px;
    overflow: hidden;
  }
  .page--summary {
    background: linear-gradient(90deg, var(--navy-deep) 0%, var(--navy) 70%, #3a5796 86%, var(--spine-light) 100%);
    color: var(--text-light);
  }
  .page-tab {
    position: absolute;
    top: 14px;
    width: 34px;
    height: 34px;
    background: var(--gold);
    color: var(--navy);
    font-size: 12px;
    font-weight: 500;
    display: flex;
    align-items: flex-end;
    justify-content: center;
    padding-bottom: 3px;
  }
  .page--summary .page-tab { left: 72px; }
  .summary-title {
    position: absolute;
    left: 140px;
    top: 52px;
    font-family: "Marcellus", Georgia, serif;
    font-size: 31px;
    font-weight: 400;
    color: var(--gold);
    letter-spacing: .5px;
  }
  .summary-columns {
    position: absolute;
    left: 140px;
    top: 100px;
    width: 350px;
    display: flex;
    gap: 10px;
    font-size: 11.2px;
    line-height: 1.38;
  }
  .summary-col { width: 170px; }
  .summary-col p + p { margin-top: 0; }
  .definitions { margin-top: 20px; font-size: 10.2px; }
  .definitions p + p { margin-top: 14px; }
  .page--photo { background: var(--paper); }
  .photo-area {
    position: absolute;
    inset: 0;
    background:
      radial-gradient(ellipse 45% 30% at 52% 78%, var(--photo-warm) 0%, rgba(217,130,111,0) 70%),
      radial-gradient(ellipse 30% 45% at 80% 65%, var(--photo-olive) 0%, rgba(95,100,72,0) 70%),
      linear-gradient(180deg, var(--photo-top) 0%, var(--photo-mid) 55%, #a79c8c 100%);
  }
  .page-number {
    position: absolute;
    left: 50%;
    bottom: 10px;
    transform: translateX(-50%);
    width: 30px;
    height: 30px;
    background: var(--navy);
    color: var(--paper);
    font-size: 12px;
    display: flex;
    align-items: center;
    justify-content: center;
  }
</style>
</head>
<body>
  <main class="spread">
    <section class="page page--summary">
      <div class="page-tab">02</div>
      <h1 class="summary-title">Executive Summary</h1>
      <div class="summary-columns">
        <div class="summary-col">
          <p>KMR Legacy Foundation (KMR) is a not-for-profit organisation that will attempt to break the cycle of homelessness. KMR will provide a live-in residence for homeless people from all age ranges and provide psychological counselling to address the issues associated with the reasons for, and impact of homelessness.</p>
          <p>It is expected that most 'Residents' will require on average twelve months in residence to address their psychological issues, during this time the Resident will be also provided with various types of training, from life-skills to specific vocational education to assist them to move towards independent living.</p>
          <p>Once the Resident is ready, KMR staff will assist the Resident with all aspects of transitioning to independent living and provide on-going assistance and support for as long as is required.</p>
          <p>KMR will cater for family groups and single parents, providing counselling for the entire family group and training for the parent. During the residency the children will attend a local school to reduce the impact to their education.</p>
          <p>KMR recognises that the cost of running the facility and providing training and work experience to a reasonably large group of people in todays economic environment will be challenging. As such, KMR is seeking funding for the initial establishment of the</p>
        </div>
        <div class="summary-col">
          <p>facility, but aims to introduce a number of separate complimentary business entities that will provide the necessary training avenue and income required with the aim of eventually being self-sustaining.</p>
          <p>Overall, KMR aims to reduce the overall incidence of homelessness Australia wide.</p>
          <div class="definitions">
            <p>Residents = homeless people living at KMR complex</p>
            <p>Clients = Residents who have been through the Program and returned to independent living, but remain in the After Care program</p>
          </div>
        </div>
      </div>
    </section>
    <section class="page page--photo">
      <div class="photo-area" role="img" aria-label="Photograph of a support worker kneeling beside a homeless man wrapped in a blanket, holding a cardboard sign reading Homeless and Hungry"></div>
      <div class="page-number">13</div>
    </section>
  </main>
</body>
</html>
```